Electrician Needs A Business Card

I already have a logo and would like a business card to be designed based around this logo the company is called Tolvane Electrical Pty Ltd

The business card will be printed on transparent plastic so I need it to stand out from the crowd. I do not want the card to have anything to do with Electrical on it eg light bulbs, power points etc

I need it to have the following details.

Gareth Pomfrey
Mobile : 0437 519 284
email : gareth@tolvaneelectrical.com.au

If it could incorporate the following onto the bottom of the card
ELECTRICAL - COMMUNICATIONS - AUDIO - VISUAL

```html
<!DOCTYPE html>
<html lang="en">
<head>
<meta charset="UTF-8">
<title>Tolvane Electrical – Business Card</title>
<link rel="stylesheet" href="https://fonts.googleapis.com/css2?family=Lato:wght@400;700&display=swap">
<style>
  :root {
    --backdrop: #6a6a6a;
    --card-white: #ffffff;
    --card-black: #0c0c0c;
    --accent-orange: #f5a81c;
    --text-dark: #1a1a1a;
    --text-light: #ffffff;
  }
  * { margin: 0; padding: 0; box-sizing: border-box; }
  html, body {
    width: 1200px;
    height: 900px;
    overflow: hidden;
    background: var(--backdrop);
    font-family: "Lato", Arial, sans-serif;
  }
  .business-card {
    position: absolute;
    left: 100px;
    top: 150px;
    width: 1000px;
    height: 600px;
    border-radius: 34px;
    overflow: hidden;
    background: var(--card-black);
  }
  .card-header {
    position: absolute;
    left: 0; top: 0;
    width: 100%;
    height: 255px;
    background: var(--card-white);
    border-bottom: 12px solid var(--accent-orange);
  }
  .brand {
    position: absolute;
    left: 200px;
    top: 88px;
    display: flex;
    align-items: center;
    gap: 28px;
  }
  .brand-square {
    width: 70px;
    height: 70px;
    background: var(--accent-orange);
  }
  .brand-name {
    font-size: 52px;
    font-weight: 400;
    color: var(--text-dark);
    letter-spacing: 0.5px;
  }
  .contact-block {
    position: absolute;
    left: 70px;
    top: 300px;
    color: var(--text-light);
  }
  .person-name {
    font-size: 46px;
    font-weight: 700;
    margin-bottom: 22px;
  }
  .contact-line {
    display: flex;
    align-items: center;
    gap: 18px;
    font-size: 30px;
    font-weight: 400;
    margin-bottom: 10px;
  }
  .contact-icon { width: 26px; height: 26px; flex: none; }
  .services {
    position: absolute;
    left: 70px;
    top: 520px;
    font-size: 32px;
    font-weight: 400;
    color: var(--accent-orange);
    letter-spacing: 1px;
    word-spacing: 4px;
  }
  .illustration-slot {
    position: absolute;
    left: 740px;
    top: 285px;
    width: 200px;
    height: 200px;
    border-radius: 8px;
    background: radial-gradient(circle at 50% 45%, #3a2a10 0%, #1a1409 55%, var(--card-black) 100%);
  }
</style>
</head>
<body>
  <div class="business-card">
    <header class="card-header">
      <div class="brand">
        <div class="brand-square"></div>
        <span class="brand-name">TOLVANE ELECTRICAL</span>
      </div>
    </header>

    <section class="contact-block">
      <h1 class="person-name">Gareth Pomfrey</h1>
      <p class="contact-line">
        <svg class="contact-icon" viewBox="0 0 24 24" aria-hidden="true">
          <path fill="#f5a81c" d="M3 8c0-2 2-4 9-4s9 2 9 4v2h-5V8H8v2H3z"/>
          <rect x="5" y="11" width="14" height="9" rx="1.5" fill="#f5a81c"/>
          <circle cx="12" cy="15.5" r="2.4" fill="#0c0c0c"/>
        </svg>
        <span>0437 519 284</span>
      </p>
      <p class="contact-line">
        <svg class="contact-icon" viewBox="0 0 24 24" aria-hidden="true">
          <rect x="2" y="5" width="20" height="14" rx="1.5" fill="#f5a81c"/>
          <path d="M2.5 6l9.5 7 9.5-7" fill="none" stroke="#0c0c0c" stroke-width="1.8"/>
        </svg>
        <span>gareth@tolvaneelectrical.com.au</span>
      </p>
    </section>

    <div class="illustration-slot" role="img" aria-label="Hand-drawn orange sketch of a glowing light bulb on black"></div>

    <p class="services">ELECTRICAL - COMMUNICATIONS - AUDIO - VISUAL</p>
  </div>
</body>
</html>
```